Need a clean & modern homepage for an education site + opportunity for longer term work

Thanks for viewing our project. We are excited about this new website and we hope that we might build a relationship with designers as we work on this project. I provided quite a few details and requirements to help you more quickly create a design that meets our needs.
Who we are:
We are a website that discusses the importance of college accreditation and provides a directory of college programs.
What we need:
A homepage that meets the below requirements and is inspired by the examples provided
Definition of accredited:
ac·cred·it·ed [uh-kred-i-tid] adj.
1. officially recognized as meeting the essential requirements, as of academic excellence: accredited schools.
2. provided with official credentials, as by a government: an accredited diplomatic representative.
3. accepted as authoritative: an accredited theory.
Overall look and feel for the homepage:
- Clean, simple and modern
- Limited (or zero) pictures
- Utilize color blocks with text
- A trend seems to be longer vertical length homepages with lots of whitespace. I generally like this trend as long as the page is not way to tall.
Inspirations: Sites that have a similar look and feel to what I need.
http://plinvar.org/
http://www.tumbrelstat.com/colleges/harrowgate-university/
http://quietmarble.org/
http://www.vellichorstaffing.com/
http://www.plonk.com/
http://sketches.zimvo.com/
Items to be included on the homepage. Details below on each item.
- Top navigation
- Logo: Please leave a blank area for a logo. The logo has not been designed.
- Simple graphic/color block at the top that highlights a definition of “Accredited” – the definition should be formatted like it is being copy/pasted from a dictionary.
- Space for a video and small (50 word) written description of the video. You can use placeholder text.
- One section with 3 Paragraphs of content (each paragraph around 100 words) with a header at the top. You can use placeholder text but please create the formatting. At the end of the 3 paragraphs please have a “Read More” Note this shouldn't be 3 separate paragraphs with three read mores - it is 3 paragraphs with one read more at the end.
- An area with the header “Search Colleges by State” that has anchor text links to all 50 states.
Top navigation:
- Home
- States – with a subnav dropdown that includes all 50 US states.
- Programs – with a subnav dropdown that includes program titles (list below)
- Degrees - with a subnav dropdown that includes 5 degree levels (list below)
- Accreditation – no subnav
- Rankings – no subnav
- Resources – no subnav
Footer
- Link to about us, privacy, and a copyright www.url.com
Programs List for sub navigation
Accounting
Art
Bible
Business
Criminal Justice
Design
Engineering
English
Law
LPN to RN
Management
Math
MBA
MPH
Medical Assisting
Military
Nursing
Occupational Therapy
Paralegal
Psychology
Pharmacy
RN to BSN
Radiology
Social Work
Sonography
Degrees list for sub navigation
Certificate
Associate
Bachelors
Masters
PhD
Thanks so much - looking forward to working with you!

```html
<!DOCTYPE html>
<html lang="en">
<head>
<meta charset="utf-8">
<title>Credovale — Homepage</title>
<link rel="stylesheet" href="https://fonts.googleapis.com/css2?family=Arimo:wght@400;700&family=PT+Sans:wght@400;700&display=swap">
<style>
  :root{
    --page:#ebe9e5;
    --band:#1b4a79;
    --band-edge:#2d5f91;
    --ink:#333130;
    --body:#5c5a57;
    --brand:#6a6966;
    --green:#5f9a10;
    --lime:#8cc20f;
    --white:#ffffff;
    --menu:#ecebe7;
    --rule:#b9b7b2;
    --btn-top:#7bb527;
    --btn-bot:#4f8a0f;
  }
  *{box-sizing:border-box;margin:0;padding:0}
  html,body{width:1200px;height:990px;overflow:hidden}
  body{position:relative;background:var(--page);font-family:"PT Sans",Tahoma,sans-serif;color:var(--body)}
  .abs{position:absolute}

  .brand{left:120px;top:14px;font-family:"PT Sans",Tahoma,sans-serif;font-weight:400;font-size:36px;line-height:1;color:var(--brand)}

  .follow{left:826px;top:51px;width:260px;height:32px;background:var(--white);border:1px solid #d3d1cc;border-bottom:none;border-radius:3px 3px 0 0;display:flex;align-items:center;padding-left:12px;gap:9px;font-family:"Arimo",Arial,sans-serif;font-size:12px;color:#444}
  .follow .label{margin-right:2px}
  .follow .social{width:22px;height:22px;border-radius:3px}
  .s1{background:#3b5b98}.s2{background:#1c6a9e}.s3{background:#4fb3dd}.s4{background:#b9b2ad}.s5{background:#3d9a1e}

  .hero{left:0;top:108px;width:1200px;height:302px;background:var(--band);border-top:4px solid var(--band-edge);border-bottom:5px solid var(--band-edge)}
  .definition{left:0;width:1200px;text-align:center;font-family:"PT Sans",Tahoma,sans-serif;font-weight:700;text-transform:uppercase;text-shadow:0 2px 2px rgba(0,0,0,.55);line-height:1;white-space:nowrap}
  .definition .w{color:var(--white)}
  .definition .g{color:var(--lime)}
  .d1{top:147px;font-size:24.5px;left:-21px}
  .d2{top:175px;font-size:29.5px;left:-20px}
  .d3{top:239px;font-size:34.5px;left:-4px}
  .d4{top:277px;font-size:23px;left:-4px}
  .d5{top:340px;font-size:24.5px;left:-18px}
  .d6{top:362px;font-size:31px;left:-18px}
  .hero-rule{left:232px;width:699px;height:1px;background:#c9d4df}

  .arrow{width:44px;height:44px}

  .nav{left:110px;top:83px;width:979px;height:42px;background:linear-gradient(#ffffff,#f1f0ed);border:1px solid #cfcdc8;border-radius:4px;display:grid;grid-template-columns:111px 114px 147px 131px 182px 141px 153px;box-shadow:0 1px 2px rgba(0,0,0,.15)}
  .nav a{display:flex;align-items:center;justify-content:center;color:var(--green);text-decoration:none;font-family:"Arimo",Arial,sans-serif;font-size:13px;text-transform:uppercase;border-right:1px solid #dcdad5;position:relative}
  .nav a:last-child{border-right:none}
  .nav a.open::after{content:"";position:absolute;bottom:0;left:50%;margin-left:-6px;border:6px solid transparent;border-bottom-color:#d9d7d2;border-top:none}

  .submenu{background:var(--menu);border:1px solid #c8c6c1;box-shadow:0 2px 5px rgba(0,0,0,.35);padding:3px 4px 0 3px;list-style:none}
  .submenu li{height:20px;border-bottom:1px solid var(--rule);padding-left:19px;font-family:"Arimo",Arial,sans-serif;font-size:11px;line-height:20px;color:#555;text-transform:uppercase}
  .submenu li:last-child{border-bottom:none}
  .programs{left:335px;top:124px;width:216px;height:308px;padding-right:12px;overflow:hidden}
  .programs .scroll{position:absolute;right:4px;top:4px;width:4px;height:299px;background:#7d7b78;border-radius:2px}
  .programs .thumb{position:absolute;right:3px;top:163px;width:6px;height:38px;background:#f4f3f0;border:1px solid #8c8a87;border-radius:2px}
  .degrees{left:482px;top:124px;width:216px;height:106px}

  h2.section{font-family:"Arimo",Arial,sans-serif;font-weight:700;font-size:18px;color:var(--ink);text-transform:uppercase;letter-spacing:.3px}
  .copy{font-size:12px;line-height:17px;text-align:justify;color:var(--body)}
  .copy p{margin-bottom:16px}

  .btn{width:96px;height:24px;border-radius:4px;background:linear-gradient(var(--btn-top),var(--btn-bot));border:1px solid #3e6e0b;color:var(--white);font-family:"Arimo",Arial,sans-serif;font-weight:700;font-size:12px;text-transform:uppercase;display:flex;align-items:center;justify-content:center;text-shadow:0 1px 1px rgba(0,0,0,.4);text-decoration:none}

  .video{left:781px;top:484px;width:276px;height:193px;background:radial-gradient(circle at 50% 50%,#4a4a4a 0%,#2a2a2a 55%,#171717 100%);display:flex;align-items:center;justify-content:center}

  .footer{left:0;top:946px;width:1200px;height:44px;background:var(--band);color:var(--white);font-family:"Arimo",Arial,sans-serif;font-size:11px;text-transform:uppercase}
  .footer .links{position:absolute;left:141px;top:16px}
  .footer .links a{color:var(--white);text-decoration:none}
  .footer .copyright{position:absolute;right:139px;top:16px}
</style>
</head>
<body>

<div class="abs brand">Credovale</div>

<div class="abs follow">
  <span class="label">FOLLOW US :</span>
  <span class="social s1" aria-hidden="true"></span>
  <span class="social s2" aria-hidden="true"></span>
  <span class="social s3" aria-hidden="true"></span>
  <span class="social s4" aria-hidden="true"></span>
  <span class="social s5" aria-hidden="true"></span>
</div>

<section class="abs hero" aria-label="Definition of accredited"></section>
<div class="abs definition d1"><span class="w">Officially recognized as meeting the essential requirements,</span></div>
<div class="abs definition d2"><span class="g">as of academic excellence: accredited schools.</span></div>
<div class="abs hero-rule" style="top:221px"></div>
<div class="abs definition d3"><span class="w">Provided with official credentials,</span></div>
<div class="abs definition d4"><span class="w">as by a government: </span><span class="g">an accredited diplomatic representative.</span></div>
<div class="abs hero-rule" style="top:318px"></div>
<div class="abs definition d5"><span class="w">Accepted as authoritative:</span></div>
<div class="abs definition d6"><span class="g">an accredited theory.</span></div>

<svg class="abs arrow" style="left:111px;top:223px" viewBox="0 0 44 44" aria-label="Previous">
  <circle cx="22" cy="22" r="21" fill="#0f2f50"/>
  <circle cx="22" cy="22" r="18.5" fill="#f4f3f0"/>
  <path d="M25 14 L17 22 L25 30" fill="none" stroke="#5f9a10" stroke-width="4.5" stroke-linecap="round" stroke-linejoin="round"/>
</svg>
<svg class="abs arrow" style="left:1045px;top:223px" viewBox="0 0 44 44" aria-label="Next">
  <circle cx="22" cy="22" r="21" fill="#0f2f50"/>
  <circle cx="22" cy="22" r="18.5" fill="#f4f3f0"/>
  <path d="M19 14 L27 22 L19 30" fill="none" stroke="#5f9a10" stroke-width="4.5" stroke-linecap="round" stroke-linejoin="round"/>
</svg>

<nav class="abs nav">
  <a href="#">Home</a>
  <a href="#">States</a>
  <a href="#" class="open">Programs</a>
  <a href="#" class="open">Degrees</a>
  <a href="#">Accreditation</a>
  <a href="#">Rankings</a>
  <a href="#">Resources</a>
</nav>

<ul class="abs submenu programs">
  <li>Accounting</li><li>Art</li><li>Bible</li><li>Business</li><li>Criminal Justice</li>
  <li>Design</li><li>Education</li><li>Engineering</li><li>English</li><li>Law</li>
  <li>LPN to RN</li><li>Management</li><li>Math</li><li>MBA</li><li>MPH</li>
  <span class="scroll"></span><span class="thumb"></span>
</ul>

<ul class="abs submenu degrees">
  <li>Certificate</li><li>Associate</li><li>Bachelors</li><li>Masters</li><li>PhD</li>
</ul>

<h2 class="abs section" style="left:141px;top:452px">Welcome</h2>
<div class="abs copy" style="left:140px;top:483px;width:569px">
  <p>Lorem Ipsum is simply dummy text of the printing and typesetting industry. Lorem Ipsum has been the industry's standard dummy text ever since the 1500s, when an unknown printer took a galley of type and scrambled it to make a type specimen book. It has survived not only five centuries, but also the leap into electronic typesetting, remaining essentially unchanged. It was popularised in the 1960s with the release of Pressmark sheets containing Lorem Ipsum passages, and more recently with desktop publishing software like Quillset Layout including versions of Lorem Ipsum.</p>
  <p>Lorem Ipsum is simply dummy text of the printing and typesetting industry. Lorem Ipsum has been the industry's standard dummy text ever since the 1500s, when an unknown printer took a galley of type and scrambled it to make a type specimen book. It has survived not only five centuries, but also the leap into electronic typesetting, remaining essentially unchanged. It was popularised in the 1960s with the release of Pressmark sheets containing Lorem Ipsum passages.</p>
  <p style="margin-top:19px">Lorem Ipsum is simply dummy text of the printing and typesetting industry. Lorem Ipsum has been the industry's standard dummy text ever since the 1500s, when an unknown printer took a galley of type and scrambled it to make a type specimen book. It has survived not only five centuries, but also the leap into electronic typesetting, remaining essentially unchanged.</p>
</div>
<a class="abs btn" href="#" style="left:613px;top:778px">Read More</a>

<h2 class="abs section" style="left:140px;top:805px">States</h2>
<div class="abs copy" style="left:140px;top:833px;width:569px">
  <p>Lorem Ipsum is simply dummy text of the printing and typesetting industry. Lorem Ipsum has been the industry's standard dummy text ever since the 1500s, when an unknown printer took a galley of type and scrambled it to make a type specimen book. It has survived not only five centuries, but also the leap into electronic typesetting, remaining essentially unchanged.</p>
</div>
<a class="abs btn" href="#" style="left:613px;top:901px">Read More</a>

<h2 class="abs section" style="left:778px;top:452px">Video</h2>
<div class="abs video" role="img" aria-label="Video player placeholder">
  <svg width="64" height="64" viewBox="0 0 64 64" aria-hidden="true">
    <circle cx="32" cy="32" r="29.5" fill="none" stroke="#fff" stroke-width="3.5"/>
    <path d="M25 18 L46 32 L25 46 Z" fill="#fff"/>
  </svg>
</div>
<div class="abs copy" style="left:778px;top:691px;width:283px">
  <p>It is a long established fact that a reader will be distracted by the readable content of a page when looking at its layout. The point of using Lorem Ipsum is that it has a more-or-less normal distribution of letters, as opposed to using 'Content here, content here', making it look like readable English.</p>
</div>
<a class="abs btn" href="#" style="left:964px;top:809px">Read More</a>

<footer class="abs footer">
  <div class="links"><a href="#">About Us</a> &nbsp;|&nbsp; <a href="#">Privacy</a></div>
  <div class="copyright">Copyright @ www.url.com</div>
</footer>

</body>
</html>
```